Buchcover-Design für Erziehungsratgeber
Zielgruppe
Es handelt sich um einen Erziehungsratgeber zum Thema 'bedürfnisorientierte Erziehung'.
Zielgruppe :
Frauen 25-35 Jahre
Werdende Mütter bzw. Mütter eines Neugeborenen
Personen mit Vorliebe für natürliche Heilmittel, Methoden oder Konzepte.
Personen, die eher Vorbehalte ggü. chemischen, kommerziellen oder industriellen Heilmitteln, Methoden, Konzepten haben.
Aufgabenstellung
Das Cover soll ein Baby 1-12 Monate zeigen, ggf. auch mit der Mutter zusammen.
Das Cover soll Schutz, Geborgenheit und Fürsorge ausstrahlen.
Eine kreativere Titel-Anordnung ist gewünscht. Bitte wählen Sie für die Titel-Anordnung KEINE Standard-Anordnung, also z.B. nicht mittig zentriert im oberen Drittel.
Farbvorschlag für den Titel-Text: 800080ff (abweichende Ideen sind trotzdem gern gesehen)
Stockmaterial wird von Bildtruhenarchiv.com bevorzugt.
Cover-Maße: 6x9 Zoll, 170 Seiten. Bitte Template benutzen.
Das Verlagslogo soll unten Links auf dem Cover abgedruckt werden. Bitte wählen Sie eine zum Cover passende, unauffällige Farbe.
Titel: 'Achtsames Aufwachsen mit Nähe und Vertrauen im ersten Lebensjahr'
Sub-Titel (unauffällig darstellen): 'So begleiten Sie Ihren Säugling mit Ruhe und Feingefühl durch die ersten Wochen und erkennen, welche Signale er Ihnen sendet. Ein Familienbegleiter für das erste Jahr mit Kind'
Autoren-Name: 'Helga Brink'

```html
<!DOCTYPE html>
<html lang="de">
<head>
<meta charset="utf-8">
<title>Achtsames Aufwachsen – Buchumschlag</title>
<link href="https://fonts.googleapis.com/css2?family=Amatic+SC:wght@700&family=Fira+Sans:wght@400;500&display=swap" rel="stylesheet">
<style>
  :root {
    --back-lilac: #bf7fbf;
    --spine-purple: #800080;
    --title-purple: #7d0a85;
    --paper-white: #ffffff;
    --imprint-grey: #4a4a4a;
  }
  html, body {
    margin: 0;
    padding: 0;
    width: 1200px;
    height: 877px;
    overflow: hidden;
    background: var(--paper-white);
  }
  .cover-wrap {
    position: relative;
    width: 1200px;
    height: 877px;
    font-family: "Fira Sans", Arial, sans-serif;
  }
  .back-cover {
    position: absolute;
    left: 0; top: 0;
    width: 581px; height: 877px;
    background: var(--back-lilac);
    color: var(--paper-white);
  }
  .back-title {
    position: absolute;
    left: 20px; top: 100px;
    width: 545px;
    margin: 0;
    text-align: center;
    font-weight: 500;
    font-size: 20px;
    line-height: 33px;
    letter-spacing: 0.8px;
    text-transform: uppercase;
    white-space: nowrap;
  }
  .back-blurb {
    position: absolute;
    left: 67px; top: 178px;
    width: 455px;
    margin: 0;
    font-size: 15px;
    line-height: 23.8px;
    letter-spacing: 0.5px;
  }
  .barcode-area {
    position: absolute;
    left: 367px; top: 728px;
    width: 191px; height: 116px;
    background: var(--paper-white);
  }
  .spine {
    position: absolute;
    left: 581px; top: 0;
    width: 36px; height: 877px;
    background: var(--spine-purple);
    color: var(--paper-white);
  }
  .spine-title, .spine-author {
    position: absolute;
    left: 50%;
    white-space: nowrap;
    font-weight: 500;
    letter-spacing: 0.8px;
    text-transform: uppercase;
    transform-origin: 0 0;
  }
  .spine-title {
    font-size: 13.5px;
    top: 624px;
    transform: rotate(-90deg) translateY(-50%);
  }
  .spine-author {
    font-size: 15px;
    top: 830px;
    transform: rotate(-90deg) translateY(-50%);
  }
  .front-cover {
    position: absolute;
    left: 617px; top: 0;
    width: 583px; height: 877px;
    overflow: hidden;
  }
  .cover-photo {
    position: absolute;
    inset: 0;
    background:
      radial-gradient(ellipse 210px 230px at 460px 230px, rgba(214,38,38,0.85), rgba(214,38,38,0) 70%),
      radial-gradient(ellipse 150px 120px at 330px 330px, rgba(238,214,196,0.9), rgba(238,214,196,0) 75%),
      radial-gradient(ellipse 120px 90px at 260px 130px, rgba(226,188,160,0.8), rgba(226,188,160,0) 75%),
      linear-gradient(180deg, #f3efee 0%, #ede6e6 35%, #f4f2f2 48%, #f7f6f5 100%);
  }
  .front-title {
    position: absolute;
    left: 43px; top: 470px;
    width: 500px; height: 230px;
    overflow: visible;
  }
  .front-title text {
    font-family: "Amatic SC", "Arial Narrow", sans-serif;
    font-weight: 700;
    fill: var(--title-purple);
  }
  .front-subtitle {
    position: absolute;
    left: 48px; top: 699px;
    width: 500px;
    margin: 0;
    font-size: 14px;
    line-height: 19px;
    letter-spacing: 0.2px;
    color: var(--title-purple);
  }
  .publisher-imprint {
    position: absolute;
    left: 36px; top: 796px;
    font-weight: 500;
    color: var(--imprint-grey);
    line-height: 1.05;
  }
  .publisher-name { display: block; font-size: 24px; }
  .publisher-word { display: block; font-size: 19px; letter-spacing: 1px; }
  .front-author {
    position: absolute;
    left: 190px; top: 814px;
    margin: 0;
    font-size: 28px;
    font-weight: 500;
    letter-spacing: 1px;
    color: var(--title-purple);
    text-transform: uppercase;
  }
</style>
</head>
<body>
<div class="cover-wrap">

  <section class="back-cover">
    <h2 class="back-title">Achtsames Aufwachsen mit Nähe<br>und Vertrauen im ersten Lebensjahr</h2>
    <p class="back-blurb">Lorem ipsum dolor sit amet, consectetuer adipiscing elit. Aenean commodo ligula eget dolor. Aenean massa. Cum sociis natoque penatibus et magnis dis parturient montes, nascetur ridiculus mus. Donec quam felis, ultricies nec, pellentesque eu, pretium quis, sem. Nulla consequat massa quis enim. Donec pede justo, fringilla vel, aliquet nec, vulputate eget, arcu. In enim justo, rhoncus ut, imperdiet a, venenatis vitae, justo. Nullam dictum felis eu pede mollis pretium. Integer tincidunt. Cras dapibus. Vivamus elementum semper nisi. Aenean vulputate eleifend tellus. Aenean leo ligula, porttitor eu, consequat vitae, eleifend ac, enim. Aliquam lorem ante, dapibus in, viverra quis, feugiat a, tellus.</p>
    <div class="barcode-area"></div>
  </section>

  <section class="spine">
    <span class="spine-title">Achtsames Aufwachsen mit Nähe und Vertrauen im ersten Lebensjahr</span>
    <span class="spine-author">Helga Brink</span>
  </section>

  <section class="front-cover">
    <div class="cover-photo" role="img" aria-label="Foto: lachende Mutter im roten Oberteil liegt auf hellem Boden und hält ihr krabbelndes Baby im weißen Strampler"></div>

    <svg class="front-title" viewBox="0 0 500 230" aria-label="Achtsames Aufwachsen mit Nähe und Vertrauen im ersten Lebensjahr">
      <text x="0" y="52" font-size="62" textLength="484" lengthAdjust="spacingAndGlyphs">ACHTSAMES AUFWACHSEN MIT NÄHE</text>
      <text x="0" y="165" font-size="140" textLength="488" lengthAdjust="spacingAndGlyphs">VERTRAUEN</text>
      <text x="0" y="216" font-size="52" textLength="488" lengthAdjust="spacingAndGlyphs">IM ERSTEN LEBENSJAHR</text>
    </svg>

    <p class="front-subtitle">So begleiten Sie Ihren Säugling mit Ruhe und Feingefühl durch die ersten Wochen und erkennen, welche Signale er Ihnen sendet.<br>Ein Familienbegleiter für das erste Jahr mit Kind</p>

    <div class="publisher-imprint"><span class="publisher-name">Wegmark</span><span class="publisher-word">Verlag</span></div>
    <p class="front-author">Helga Brink</p>
  </section>

</div>
</body>
</html>
```